New Townhome community needs for sale sign.

need a 4 foot by 8 foot banner to put on building listing newly constructed townhomes as "coming soon" to market. Construction is scheduled to be completed Dec 2024. Sale of units will begin Spring of 2025.
6 individual townhome units each 2,000 square feet. each unit is 3 bedroom 2.5 bathroom with 2 car garage and each has a rooftop "sky lounge" with amazing views. Gated community. Units available for sale Spring of 2025. Real estate company selling units will be KLM & Partners. Will need KLM & Partners Logo on the banner. Would like to keep with the same blue color scheme as the KLM & Partners logo. phone number on banner to be 602-555-4179. web klmpartnersx.com.

```html
<!DOCTYPE html>
<html lang="en">
<head>
<meta charset="utf-8">
<title>Coming Soon – Townhomes For Sale Banner</title>
<link href="https://fonts.googleapis.com/css2?family=Montserrat:wght@400;500;600;700;800&display=swap" rel="stylesheet">
<style>
  :root {
    --brand-blue: #1f74a8;
    --sky-blue: #3cbef0;
    --badge-blue: #29a8dc;
    --navy: #1c5b8b;
    --band-black: #1b1b1b;
    --pill-dark: #333538;
    --white: #ffffff;
    --page: #e9ebed;
    --ink: #1e1e1e;
  }
  * { box-sizing: border-box; margin: 0; padding: 0; }
  html, body {
    width: 913px; height: 1200px; overflow: hidden;
    background: var(--page);
    font-family: "Montserrat", sans-serif;
  }
  .banner {
    position: absolute; left: 30px; top: 386px;
    width: 853px; height: 427px;
    background: var(--white);
    box-shadow: 0 10px 24px rgba(0,0,0,.18);
  }
  .headline-panel {
    position: absolute; left: 0; top: 0; width: 853px; height: 208px;
    background: var(--brand-blue);
    text-align: center; color: var(--white);
  }
  .headline-main {
    position: absolute; left: 0; right: 0; top: 18px;
    font-size: 80px; font-weight: 800; line-height: 1;
    color: var(--sky-blue); letter-spacing: -0.5px;
    text-shadow: 3px 3px 0 #175d88;
  }
  .headline-sub {
    position: absolute; left: 0; right: 0; top: 110px;
    font-size: 38px; font-weight: 400; line-height: 1;
  }
  .headline-offer {
    position: absolute; left: 0; right: 0; top: 148px;
    font-size: 46px; font-weight: 800; line-height: 1;
    text-shadow: 2px 2px 0 #174f75;
  }
  .features-band {
    position: absolute; left: 0; top: 208px; width: 853px; height: 127px;
    background: var(--band-black); color: var(--white);
  }
  .stat-box {
    position: absolute; top: 12px; height: 51px;
    border: 1px solid #6d6d6d; border-radius: 3px;
    display: flex; align-items: center;
  }
  .stat-units { left: 58px; width: 231px; padding-left: 14px; }
  .stat-area { left: 301px; width: 324px; padding-left: 13px; }
  .stat-number { font-weight: 700; line-height: 1; margin-right: 10px; }
  .stat-units .stat-number { font-size: 36px; }
  .stat-area .stat-number { font-size: 40px; }
  .stat-label {
    font-size: 16px; font-weight: 700; line-height: 1.05;
    color: var(--sky-blue); text-transform: uppercase;
  }
  .spec-row {
    position: absolute; left: 60px; top: 76px;
    display: flex; align-items: center; gap: 8px;
    font-size: 15px; font-weight: 500; white-space: nowrap;
  }
  .unit-tag {
    background: var(--badge-blue); padding: 1px 7px; margin-right: 6px;
    font-size: 14px; font-weight: 500;
  }
  .spec { display: flex; align-items: center; gap: 4px; margin-right: 10px; }
  .spec svg { width: 20px; height: 16px; fill: var(--badge-blue); }
  .amenity-row {
    position: absolute; left: 60px; top: 102px;
    font-size: 15px; font-weight: 500; white-space: nowrap;
    color: var(--sky-blue);
  }
  .amenity-row .accent { color: var(--white); }
  .amenity-row .divider { color: var(--white); margin: 0 6px 0 10px; }
  .availability {
    position: absolute; left: 679px; top: 193px; width: 144px; height: 142px;
    background: var(--badge-blue); color: var(--white); text-align: center;
    padding-top: 9px;
  }
  .availability-label { font-size: 17px; font-weight: 500; line-height: 1.1; text-transform: uppercase; }
  .availability-season { margin-top: 6px; font-size: 17px; font-weight: 800; line-height: 1; }
  .availability-year { font-size: 30px; font-weight: 800; line-height: 1.05; }
  .brand {
    position: absolute; left: 83px; top: 358px;
    display: flex; align-items: center; gap: 10px;
  }
  .brand-mark { width: 34px; height: 34px; background: var(--brand-blue); }
  .brand-name { font-size: 28px; font-weight: 700; color: var(--navy); }
  .contact {
    position: absolute; left: 388px; top: 344px; width: 410px; text-align: center;
  }
  .contact-intro { font-size: 12.5px; font-weight: 500; color: var(--ink); }
  .contact-pill {
    margin-top: 5px; height: 26px; border-radius: 13px;
    display: flex; position: relative; background: var(--pill-dark);
  }
  .contact-phone, .contact-web {
    font-size: 16px; font-weight: 700; color: var(--white); line-height: 26px;
    white-space: nowrap;
  }
  .contact-phone {
    background: var(--brand-blue); width: 178px; border-radius: 13px 0 0 13px;
    padding-right: 14px;
  }
  .contact-web { flex: 1; padding-left: 24px; padding-right: 10px; text-align: center; }
  .contact-icon {
    position: absolute; left: 164px; top: -1px; width: 28px; height: 28px;
    border-radius: 50%; background: var(--brand-blue); border: 2px solid var(--white);
    display: flex; align-items: center; justify-content: center;
  }
  .contact-icon svg { width: 12px; height: 15px; }
  .completion-note {
    margin-top: 6px; font-size: 11.5px; font-weight: 700; color: var(--navy);
    text-transform: uppercase;
  }
</style>
</head>
<body>
<main class="banner">
  <section class="headline-panel">
    <h1 class="headline-main">COMING SOON</h1>
    <p class="headline-sub">NEWLY CONSTRUCTED</p>
    <p class="headline-offer">TOWNHOMES FOR SALE</p>
  </section>

  <section class="features-band">
    <div class="stat-box stat-units">
      <span class="stat-number">6</span>
      <span class="stat-label">Individual<br>Townhome Units</span>
    </div>
    <div class="stat-box stat-area">
      <span class="stat-number">2,000</span>
      <span class="stat-label">Square Feets<br>Each Unit Area</span>
    </div>

    <div class="spec-row">
      <span class="unit-tag">EACH UNIT</span>
      <span class="spec">
        <svg viewBox="0 0 20 16" aria-hidden="true"><rect x="3" y="1" width="14" height="6" rx="1"/><rect x="1" y="8" width="18" height="5" rx="1"/><rect x="1" y="13" width="2" height="3"/><rect x="17" y="13" width="2" height="3"/></svg>
        3 BEDROOM
      </span>
      <span class="spec">
        <svg viewBox="0 0 20 16" aria-hidden="true"><rect x="0" y="5" width="20" height="2"/><path d="M1 7h18l-2 6H3z"/><rect x="3" y="13" width="2" height="3"/><rect x="15" y="13" width="2" height="3"/></svg>
        2.5 BATHROOM
      </span>
      <span class="spec">
        <svg viewBox="0 0 20 16" aria-hidden="true"><path d="M10 0L0 5v2l10-5 10 5V5z"/><path d="M4 9l2-3h8l2 3v5h-2v-2H6v2H4z"/></svg>
        2 CAR GARAGE
      </span>
    </div>
    <p class="amenity-row">ROOFTOP <span class="accent">“SKY LOUNGE”</span> WITH AMAZING VIEWS<span class="divider">|</span>GATED COMMUNITY</p>
  </section>

  <aside class="availability">
    <p class="availability-label">Units<br>Available<br>For Sale</p>
    <p class="availability-season">SPRING OF</p>
    <p class="availability-year">2025</p>
  </aside>

  <div class="brand">
    <span class="brand-mark"></span>
    <span class="brand-name">KLM &amp; Partners</span>
  </div>

  <section class="contact">
    <p class="contact-intro">for more information and inquries, please contact :</p>
    <div class="contact-pill">
      <span class="contact-phone">602-555-4179</span>
      <span class="contact-web">KLMPARTNERSX.COM</span>
      <span class="contact-icon">
        <svg viewBox="0 0 12 15" aria-hidden="true"><rect x="1" y="0.5" width="10" height="14" rx="2" fill="none" stroke="#fff" stroke-width="1.6"/><circle cx="6" cy="11.5" r="1" fill="#fff"/></svg>
      </span>
    </div>
    <p class="completion-note">Construction will be completed Dec 2024</p>
  </section>
</main>
</body>
</html>
```